Vale Crest Motors Business Card

Would like a cutting edge / high end Automotive Business card design. Please see current card which is old and dated. Would like to maintain the Vale Crest Motors logo and same information (address, website, etc).

See our website for the look and feel of what we offer - www.valecrestmotors.example

Target Market(s)

Upper class car buyers

Contact Information for Business Card

Modern high end business card design

Requirements
Nice to have
• Carbon Fiber look background

```html
<!DOCTYPE html>
<html lang="en">
<head>
<meta charset="UTF-8">
<title>Vale Crest Motors Business Card</title>
<link href="https://fonts.googleapis.com/css2?family=Poppins:wght@300;400&family=Tinos&display=swap" rel="stylesheet">
<style>
  :root {
    --backdrop: #d9d9d9;
    --card: #1b1b1b;
    --card-edge: #242424;
    --ink: #f2f2f2;
    --ink-soft: #cfcfcf;
  }
  * { margin: 0; padding: 0; box-sizing: border-box; }
  html, body {
    width: 1200px;
    height: 800px;
    overflow: hidden;
    background: var(--backdrop);
  }
  .canvas {
    position: relative;
    width: 1200px;
    height: 800px;
    display: flex;
    justify-content: center;
    align-items: center;
    gap: 60px;
  }
  .card {
    position: relative;
    width: 500px;
    height: 286px;
    background: var(--card);
    border: 1px solid var(--card-edge);
    color: var(--ink);
    font-family: 'Poppins', sans-serif;
    display: flex;
    flex-direction: column;
    align-items: center;
    text-align: center;
    box-shadow: 0 14px 30px rgba(0,0,0,0.25);
  }
  .brand-name {
    font-family: 'Poppins', sans-serif;
    font-weight: 400;
    color: var(--ink);
    letter-spacing: 0.14em;
    text-transform: uppercase;
    display: flex;
    align-items: center;
    gap: 10px;
  }
  .brand-dot {
    width: 8px;
    height: 8px;
    border-radius: 50%;
    background: var(--ink);
  }
  /* front */
  .card-front { padding-top: 70px; }
  .card-front .brand-name { font-size: 26px; }
  .tagline {
    margin-top: 18px;
    font-size: 13px;
    font-weight: 300;
    line-height: 1.35;
    color: var(--ink-soft);
  }
  .values {
    position: absolute;
    bottom: 32px;
    left: 0;
    right: 0;
    display: flex;
    justify-content: center;
    align-items: center;
    gap: 18px;
    font-size: 10px;
    font-weight: 300;
    letter-spacing: 0.08em;
    color: var(--ink-soft);
  }
  .values .divider {
    width: 2px;
    height: 12px;
    background: var(--ink);
  }
  /* back */
  .card-back { padding-top: 44px; }
  .card-back .brand-name { font-size: 22px; }
  .person-name {
    margin-top: 22px;
    font-family: 'Tinos', serif;
    font-size: 24px;
    line-height: 1;
  }
  .person-role {
    font-size: 11px;
    font-weight: 300;
    color: var(--ink-soft);
    margin-top: 2px;
  }
  .contact {
    margin-top: 20px;
    font-size: 10px;
    font-weight: 300;
    line-height: 1.5;
    color: var(--ink-soft);
  }
  .rule {
    width: 10px;
    height: 2px;
    background: var(--ink);
    margin: 8px auto;
  }
  .address {
    font-size: 10px;
    font-weight: 300;
    line-height: 1.5;
    color: var(--ink-soft);
  }
</style>
</head>
<body>
  <main class="canvas">
    <section class="card card-front" aria-label="Card front">
      <div class="brand-name"><span class="brand-dot"></span>Vale Crest Motors</div>
      <p class="tagline">Offering the Finest in<br>Luxury and Exotic<br>Sports Cars</p>
      <div class="values">
        <span>QUALITY</span><span class="divider"></span>
        <span>INTEGRITY</span><span class="divider"></span>
        <span>SERVICE</span>
      </div>
    </section>

    <section class="card card-back" aria-label="Card back">
      <div class="brand-name"><span class="brand-dot"></span>Vale Crest Motors</div>
      <h1 class="person-name">Daniel Orrin</h1>
      <p class="person-role">owner</p>
      <p class="contact">
        t. (555) 014-2870 &nbsp;f. (555) 014-2871<br>
        e. daniel@valecrestmotors.example &nbsp;w. www.valecrestmotors.example
      </p>
      <div class="rule"></div>
      <p class="address">1180 Harbor Ridge Road B<br>Alder Bay CA 90210</p>
    </section>
  </main>
</body>
</html>
```